A-Stand Directional Sign Design

Objective:
We need a professional graphic design for an A-Stand sign that will guide customers arriving in our parking lot to our office. The design should be visually clear, welcoming, and aligned with our brand identity.
REQUIREMENTS:
Two versions of the design:
- One with an arrow pointing left
- One with an arrow pointing right
(This allows us to place the A-Stand anywhere and flip the graphic as needed.)
DIMENSIONS:
- Viewable Area: 30" x 40"
BRAND ALIGNMENT:
- Colors, fonts, and overall style should match our website: www.skornabel.com
- Clean, modern, and professional look consistent with our aviation/tourism brand
CONTENT:
- Clear directional arrow (left or right depending on version)
- Text: “Office Entrance” or similar concise wording (designers may propose alternatives if they improve clarity)
READABILITY:
- Bold, high-contrast design for visibility from a distance
- Simple layout that avoids clutter
DELIVERABLES:
- Final artwork in print-ready format (PDF preferred)
- Two versions: Arrow Left and Arrow Right
DESIGN GOAL:
Ensure customers can easily find our office upon arrival, while reinforcing skorNABEL’s professional and welcoming brand image.
Target Market(s)
Tourism

```html
<!DOCTYPE html>
<html lang="en">
<head>
<meta charset="utf-8">
<title>skorNABEL – Entrance A-Stand Signs</title>
<link href="https://fonts.googleapis.com/css2?family=Montserrat:wght@800;900&display=swap" rel="stylesheet">
<style>
  :root {
    --backdrop: #c4c4c4;
    --sign-white: #ffffff;
    --brand-blue: #2b7bba;
    --band-dark: #292e35;
    --chevron-light: #9dbde4;
    --chevron-mid: #4f7bbf;
    --chevron-white: #ffffff;
  }
  * { margin: 0; padding: 0; box-sizing: border-box; }
  html, body { width: 1200px; height: 825px; overflow: hidden; }
  body {
    background: var(--backdrop);
    font-family: "Montserrat", Arial, sans-serif;
    position: relative;
  }
  .sign {
    position: absolute;
    top: 77px;
    width: 502px;
    height: 670px;
    background: var(--sign-white);
    overflow: hidden;
  }
  .sign--left { left: 70px; }
  .sign--right { left: 628px; }

  .brand {
    position: absolute;
    top: 120px;
    left: 0;
    width: 100%;
    display: flex;
    justify-content: center;
    align-items: center;
    gap: 14px;
  }
  .brand__dot {
    width: 26px;
    height: 26px;
    border-radius: 50%;
    background: var(--brand-blue);
  }
  .brand__name {
    font-weight: 800;
    font-size: 58px;
    color: var(--brand-blue);
    line-height: 1;
  }

  .tagline {
    position: absolute;
    top: 295px;
    left: 0;
    width: 100%;
    text-align: center;
    font-weight: 900;
    font-size: 64px;
    line-height: 66px;
    color: var(--brand-blue);
    letter-spacing: 0.5px;
  }

  .direction-band {
    position: absolute;
    left: 0;
    top: 463px;
    width: 100%;
    height: 207px;
    background: var(--band-dark);
  }
  .direction-band__label {
    position: absolute;
    top: 30px;
    left: 0;
    width: 100%;
    text-align: center;
    font-weight: 800;
    font-size: 52px;
    letter-spacing: 9px;
    padding-left: 9px;
    color: var(--sign-white);
    line-height: 1;
  }
  .direction-band__arrows {
    position: absolute;
    top: 107px;
    left: 162px;
    width: 186px;
    height: 75px;
  }
  .chevron { fill: none; stroke-width: 20; stroke-linecap: round; stroke-linejoin: round; }
  .chevron--white { stroke: var(--chevron-white); }
  .chevron--light { stroke: var(--chevron-light); }
  .chevron--mid { stroke: var(--chevron-mid); }
</style>
</head>
<body>

  <section class="sign sign--left" aria-label="Entrance sign, arrow left">
    <div class="brand">
      <span class="brand__dot"></span>
      <span class="brand__name">skorNABEL</span>
    </div>
    <h1 class="tagline">WE CREATE<br>MEMORIES</h1>
    <div class="direction-band">
      <p class="direction-band__label">ENTRANCE</p>
      <svg class="direction-band__arrows" viewBox="0 0 186 75" aria-label="Arrows pointing left">
        <polyline class="chevron chevron--white" points="42,10 12,37.5 42,65"/>
        <polyline class="chevron chevron--light" points="109,10 79,37.5 109,65"/>
        <polyline class="chevron chevron--mid" points="176,10 146,37.5 176,65"/>
      </svg>
    </div>
  </section>

  <section class="sign sign--right" aria-label="Entrance sign, arrow right">
    <div class="brand">
      <span class="brand__dot"></span>
      <span class="brand__name">skorNABEL</span>
    </div>
    <h1 class="tagline">WE CREATE<br>MEMORIES</h1>
    <div class="direction-band">
      <p class="direction-band__label">ENTRANCE</p>
      <svg class="direction-band__arrows" viewBox="0 0 186 75" aria-label="Arrows pointing right">
        <polyline class="chevron chevron--mid" points="10,10 40,37.5 10,65"/>
        <polyline class="chevron chevron--light" points="77,10 107,37.5 77,65"/>
        <polyline class="chevron chevron--white" points="144,10 174,37.5 144,65"/>
      </svg>
    </div>
  </section>

</body>
</html>
```